Brochure design

I have attached our current prospectus which has been created by ourselves, we are looking for this now to be professionally designed. We are happy to use the content but also for this to be amended to co-incide with the message on our website www.tinkleford.co.uk and for it to be condensed into a more reader friendly format. Whilst we are happy with this website, again it was created by ourselves and we are not necessarily following the same design features but the colour scheme should be similar to the website. The prospectus will be printed on 2 x A4 sheets folded to make an 8 page A5 booklet with page 1 being a front cover and page 8 being back cover with contact information. The business is a childrens day nursery so the prospectus should be bright, fun, to the point and informative. I am happy to provide any further information to designers who may be looking at this by emailing me dana@tinkleford.co.uk . The completed product should allow us to edit the text for example to communicate price changes.

Further information:

Tinkleford Nursery is very unique compared with other Nurseries. Most nurseries segregate age groups into different rooms whereas at Tinkleford aged groups mix together to create a homely environment and also children are not moving through different rooms every year. Could we therefore get a message through the prospectus which reflects this, we currently use a strapline "A unique home from home childcare experience" but we are looking to change this and will be grateful for ideas.

We have no preference whether stock images are used or our own, However, stock images and ours should not be included on the same page.

From the designs received we do like stock images for the front and back cover but these must be relevant, ie showing children aged 3 months old to 5 years old.

Target Market(s)

Mum's mainly but Dad's also of children aged 0 to 5 years old. Age range of parents between 22 and 45.

Industry/Entity Type

Environment

Font styles to use
Serif

Colors
acd036
b768aa
e9f1ce
ecdaeb
ceeae6

Requirements
Must have
• Fun, Colorfull, Bright, Concise, Informative.
Should not have
• Stock images and supplied images on the same pages

```html
<!DOCTYPE html>
<html lang="en">
<head>
<meta charset="utf-8">
<title>Tinkleford Nursery Prospectus – Covers</title>
<link rel="stylesheet" href="https://fonts.googleapis.com/css2?family=Arimo:wght@700&family=Open+Sans:wght@700&display=swap">
<style>
  :root {
    --backdrop: #efeae4;
    --purple: #a0579a;
    --purple-soft: #b768aa;
    --lime: #8cc63f;
    --lime-deep: #6aa92a;
    --leaf: #3f5f2a;
    --pink: #e0637a;
    --sky: #dcebf7;
    --white: #ffffff;
    --ink: #111111;
  }
  * { box-sizing: border-box; margin: 0; padding: 0; }
  html, body { width: 1200px; height: 900px; overflow: hidden; }
  body { background: var(--backdrop); position: relative; }

  .spread {
    position: absolute; left: 90px; top: 100px;
    width: 1022px; height: 722px;
    box-shadow: 0 4px 14px rgba(0,0,0,.18);
  }
  .page { position: absolute; top: 0; height: 722px; overflow: hidden; }
  .page--back { left: 0; width: 510px; background: linear-gradient(180deg, #ffffff 30%, var(--sky) 70%, #ffffff 100%); }
  .page--front { left: 510px; width: 512px; background: var(--white); }

  .photo { position: absolute; }
  .shape { position: absolute; left: 0; top: 0; }

  .back-team { left: 0; top: 0; width: 510px; height: 175px;
    background: linear-gradient(90deg, #9a4f95, var(--purple-soft) 50%, #8e4889); }

  .masthead { position: absolute; text-align: center; font-family: "Arimo", sans-serif; font-weight: 700; font-style: normal; line-height: 1; }
  .masthead__name { color: var(--pink); font-size: 40px; display: inline-flex; align-items: center; gap: 10px; }
  .masthead__dot { width: 14px; height: 14px; border-radius: 50%; background: var(--pink); display: inline-block; }
  .masthead__title { color: var(--purple); font-size: 24px; letter-spacing: 4px; margin-top: 12px; text-transform: uppercase; }
  .page--back .masthead { left: 0; width: 510px; top: 238px; }
  .page--front .masthead { left: 60px; width: 400px; top: 34px; }

  .contact { position: absolute; left: 0; width: 510px; top: 366px; text-align: center;
    font-family: "Arimo", sans-serif; font-weight: 700; font-style: normal; color: var(--ink); }
  .contact__heading { color: var(--leaf); font-size: 29px; margin-bottom: 10px; }
  .contact__line { font-size: 21px; line-height: 31px; }
  .contact__phone { font-size: 27px; line-height: 34px; }
  .contact__email { font-size: 20px; line-height: 30px; }

  .meadow { left: 0; top: 540px; width: 100%; height: 182px;
    background: linear-gradient(180deg, rgba(140,198,63,0) 0%, #a6d45a 30%, #6fb52f 70%, #5aa123 100%); }

  .site { position: absolute; left: 0; width: 100%; top: 683px; text-align: center;
    font-family: "Arimo", sans-serif; font-weight: 700; font-size: 20px; color: var(--white); }

  .front-building { left: 0; top: 110px; width: 512px; height: 380px;
    background: linear-gradient(180deg, #b0684f 0%, #c9894f 45%, #6d6a68 75%, #5a5856 100%); }
  .front-lawn { left: 0; top: 470px; width: 512px; height: 252px;
    background: linear-gradient(180deg, #acd036 0%, #8cc63f 45%, #5aa123 100%); }

  .polaroid { position: absolute; background: var(--white); padding: 7px;
    box-shadow: 0 3px 8px rgba(0,0,0,.3); }
  .polaroid .photo { position: static; width: 100%; height: 100%; }
  .polaroid--play { left: 135px; top: 340px; width: 275px; height: 188px; transform: rotate(-1.5deg); }
  .polaroid--play .photo { background: linear-gradient(160deg, #9a8b7a, #c7b39d 60%, #7d8a6a); }
  .polaroid--sand { left: 2px; top: 432px; width: 192px; height: 162px; transform: rotate(-8deg); }
  .polaroid--sand .photo { background: linear-gradient(160deg, #7fa16a, #c79a6a 55%, #b3875a); }
  .polaroid--visit { left: 314px; top: 440px; width: 190px; height: 160px; transform: rotate(9deg); }
  .polaroid--visit .photo { background: linear-gradient(160deg, #d8c7b8, #c0392b 55%, #e9e2da); }

  .headline { position: absolute; left: 0; width: 512px; top: 600px; text-align: center;
    font-family: "Open Sans", sans-serif; font-weight: 700; font-size: 31px; line-height: 34px;
    color: var(--white); text-shadow: 0 1px 3px rgba(0,0,0,.35); }
</style>
</head>
<body>
  <main class="spread">
    <section class="page page--back">
      <div class="photo back-team" role="img" aria-label="Group photo of the nursery staff team"></div>
      <svg class="shape" width="510" height="200" viewBox="0 0 510 200" aria-hidden="true">
        <path d="M0 155 C140 140 340 140 510 80 L510 200 L0 200 Z" fill="var(--lime)"/>
        <path d="M0 175 C150 158 350 160 510 105 L510 200 L0 200 Z" fill="#ffffff"/>
      </svg>

      <div class="masthead">
        <div class="masthead__name"><span class="masthead__dot"></span>Tinkleford</div>
        <div class="masthead__title">Prospectus</div>
      </div>

      <div class="contact">
        <div class="contact__heading">CONTACT US</div>
        <div class="contact__line">12 Willowmead Close</div>
        <div class="contact__line">Brookhaven BH4 2QT</div>
        <div class="contact__phone">01632960418</div>
        <div class="contact__email">Enquiries@tinkleford.co.uk</div>
      </div>

      <div class="photo meadow" role="img" aria-label="Illustrated grass meadow with flowers and dew drops"></div>
      <div class="site">www.tinkleford.co.uk</div>
    </section>

    <section class="page page--front">
      <div class="photo front-building" role="img" aria-label="Photo of the nursery building entrance and fenced yard"></div>
      <div class="photo front-lawn" role="img" aria-label="Illustrated grass meadow with flowers"></div>
      <svg class="shape" width="512" height="722" viewBox="0 0 512 722" aria-hidden="true">
        <path d="M0 0 L512 0 L512 140 C400 175 260 185 160 160 C90 142 40 115 0 90 Z" fill="var(--purple-soft)"/>
        <path d="M0 0 L512 0 L512 118 C400 160 260 168 165 144 C95 126 42 100 0 75 Z" fill="#ffffff"/>
        <path d="M0 420 C60 440 140 455 260 445 C360 437 440 430 512 440 L512 470 C430 462 360 470 260 478 C150 486 70 480 0 470 Z" fill="var(--purple-soft)"/>
        <path d="M0 470 C70 480 150 486 260 478 C360 470 430 462 512 470 L512 722 L0 722 Z" fill="var(--lime)" opacity=".55"/>
      </svg>

      <div class="masthead">
        <div class="masthead__name"><span class="masthead__dot"></span>Tinkleford</div>
        <div class="masthead__title">Prospectus</div>
      </div>

      <figure class="polaroid polaroid--play"><div class="photo" role="img" aria-label="Photo of toddlers playing on the floor"></div></figure>
      <figure class="polaroid polaroid--sand"><div class="photo" role="img" aria-label="Photo of a child playing in a sandpit"></div></figure>
      <figure class="polaroid polaroid--visit"><div class="photo" role="img" aria-label="Photo of children at a Christmas visit"></div></figure>

      <h1 class="headline">EXCEEDING YOUR<br>EXPECTATION OF CHILDCARE</h1>
      <div class="site">www.tinkleford.co.uk</div>
    </section>
  </main>
</body>
</html>
```